lab equipment website

We need a fresh new look for a company website called quorvin. We will be using the current logo and brand colors on their current website quorvin.com. They want to keep their text and on-page SEO, but would like to reformat it to look more modern and fresh. They want to have everything be high performance with a great user experience. Their main call to action is for people to fill in a contact form so they can call them. There is some information that is purposely above the fold on the instrument pages. I will need the home page, about page and a leasing page.

```html
<!DOCTYPE html>
<html lang="en">
<head>
<meta charset="utf-8">
<title>quorvin – lab equipment website pages</title>
<link rel="stylesheet" href="https://fonts.googleapis.com/css2?family=Roboto:wght@300;400;500;700&display=swap">
<style>
:root{
  --teal:#33c4ad;
  --teal-deep:#27a893;
  --ink:#3a3c40;
  --bar:#3b3d41;
  --head:#46484c;
  --panel:#2e3033;
  --mint:#eef7f5;
  --mint-2:#e2f2ee;
  --line:#d6e2df;
  --muted:#8c9694;
  --alert:#e23b2e;
  --white:#ffffff;
}
*{box-sizing:border-box;margin:0;padding:0}
html,body{width:1200px;height:1200px;overflow:hidden;background:var(--white);font-family:"Roboto",sans-serif;color:var(--ink)}
.canvas{position:relative;width:1200px;height:1200px;overflow:hidden}
.page{position:absolute;overflow:hidden;background:linear-gradient(180deg,#f6fbfa 0%,var(--mint) 100%);box-shadow:0 0 0 6px rgba(230,238,236,.7)}
.page > *{position:absolute}
.topbar{left:0;top:0;width:100%;background:var(--bar);color:#cfd3d2;white-space:nowrap}
.topbar .dot{display:inline-block;border-radius:50%;background:#e4e7e6;margin-right:2px;vertical-align:middle}
.topbar .phone{color:var(--teal);font-weight:500}
.header{left:0;width:100%;background:var(--head)}
.brand{color:var(--white);font-weight:700;display:flex;align-items:center;gap:3px;position:absolute}
.brand i{display:inline-block;border-radius:50%;background:var(--teal)}
.nav-item{position:absolute;top:0;height:100%;color:#c8cccb;text-align:center;text-transform:uppercase}
.nav-item.active{background:#eef1f0;color:var(--teal)}
.nav-item b{display:block;margin:0 auto;border-radius:50%;background:currentColor;opacity:.8}
.cart{position:absolute;top:0;height:100%;background:var(--teal);display:flex;align-items:center;justify-content:center}
.search-hint{font-weight:700;color:var(--teal);white-space:nowrap}
.search-hint span{color:var(--ink);font-weight:500}
.search-box{background:var(--white);border:1px solid var(--line);color:#aab}
.search-btn{background:var(--bar)}
.backdrop{background:radial-gradient(ellipse at 30% 40%,#dfe9e8 0%,rgba(238,247,245,0) 70%)}
.hero-title{font-weight:300;white-space:nowrap}
.hero-accent{font-weight:700;color:var(--teal);white-space:nowrap}
.hero-accent em{font-style:normal;color:var(--ink)}
.hero-copy{color:#555;line-height:1.5}
.btn{display:flex;align-items:center;justify-content:center;color:var(--white);font-weight:500;text-transform:uppercase;white-space:nowrap}
.btn.teal{background:var(--teal)}
.btn.dark{background:var(--panel)}
.flag{outline:2px solid var(--alert);outline-offset:1px}
.hero-visual{background:linear-gradient(135deg,#f2f5f5 0%,#c9d1d2 55%,#9aa3a6 100%);border-radius:4px}
.card{border:1px solid #e2e7e6;background:#fff}
.card .shot{position:absolute;left:6%;top:6%;width:88%;height:72%;background:linear-gradient(160deg,#fafbfb,#c7ccce);border-radius:2px}
.card .label{position:absolute;left:0;width:100%;text-align:center;font-weight:500;text-transform:uppercase;color:var(--ink)}
.card.active{border:2px solid var(--teal)}
.card.active .label{color:var(--teal)}
.card .pin{position:absolute;left:50%;bottom:0;transform:translate(-50%,50%) rotate(45deg);background:var(--panel)}
.card.active .pin{background:var(--teal)}
.dots{display:flex;gap:4px}
.dots i{display:block;border-radius:50%;border:1px solid var(--teal)}
.dots i:first-child{background:var(--teal)}
.hours-band{background:var(--teal);color:#fff;text-align:center;font-weight:500}
.hours-badge{background:#fff;border:2px solid var(--teal);clip-path:polygon(25% 3%,75% 3%,100% 50%,75% 97%,25% 97%,0 50%)}
.hours-row{display:flex;justify-content:space-between;border-bottom:1px solid var(--line)}
.hours-row .t{color:var(--teal)}
.hours-row .closed{color:var(--alert)}
.caps{text-transform:uppercase;font-weight:700;color:#666;letter-spacing:.16em}
.caps b{color:var(--teal)}
.copy{color:#777;line-height:1.6;text-align:center}
.copy.left{text-align:left}
.form{background:var(--panel);border:1px solid #555}
.form > *{position:absolute}
.form .ttl{color:#fff;font-weight:700;letter-spacing:.12em;text-transform:uppercase;line-height:1.3}
.form .ttl b{color:var(--teal)}
.tab{display:flex;align-items:center;justify-content:center;color:#fff}
.tab.on{background:var(--teal)}
.tab.off{background:#3c3e42}
.form .sub{color:#ddd;letter-spacing:.18em;text-transform:uppercase;font-weight:500}
.field{border:1px solid #4a4c50;background:#313336;color:#6e7272;display:flex;align-items:center;justify-content:center}
.submit{background:var(--teal);color:#fff;display:flex;align-items:center;justify-content:center;font-weight:700}
.side-head{background:var(--teal);color:#fff;font-weight:700;display:flex;align-items:center}
.side-list li{list-style:none;border-bottom:1px solid #e3ebe9;color:#666;text-transform:uppercase}
.side-list li.on{background:#e6eceb;color:var(--ink);font-weight:700}
.body-title{color:var(--teal);font-weight:400;letter-spacing:.18em}
.rows li{list-style:none;border-bottom:1px solid #e0e7e5;color:#777}
.footer{left:0;width:100%;background:var(--bar);color:#ccc}
.footer > *{position:absolute}
.footer h4{color:#fff;font-weight:700;text-transform:uppercase}
.footer .legal{left:0;width:100%;text-align:center;color:#999;background:var(--panel)}
.badge-num{width:54px;height:54px;border-radius:50%;background:var(--teal-deep);color:#fff;font-weight:700;font-size:34px;display:flex;align-items:center;justify-content:center;border:3px solid #fff}
.legend{position:absolute;left:90px;top:1010px;width:632px;height:190px;background:#3a3b3f;color:#fff;font-size:22px}
.legend p{position:absolute;left:54px;white-space:nowrap}
.legend b{font-weight:700}
.legend span{position:absolute;left:186px}
.photo{background:linear-gradient(180deg,#c9cfd0,#8d9597)}
.avatar{border-radius:50%;background:#a7aeb0;border:2px solid #fff}
.skill-icon{border-radius:50%;background:var(--teal)}
.progress{background:#dde5e3;height:3px}
.progress i{display:block;height:100%;background:var(--teal)}
.tiny{font-size:3.6px;line-height:1.6;color:#888}
</style>
</head>
<body>
<div class="canvas">

<!-- ============ PAGE 1 : LANDING ============ -->
<section class="page landing" style="left:16px;top:12px;width:560px;height:612px">
  <div class="topbar" style="height:18px;font-size:4px;line-height:18px">
    <span style="position:absolute;left:78px"><i class="dot" style="width:8px;height:8px"></i><i class="dot" style="width:8px;height:8px"></i><i class="dot" style="width:8px;height:8px"></i><i class="dot" style="width:8px;height:8px"></i></span>
    <span style="position:absolute;left:154px">48 Alder Lane Suite 300 Fremont, CA 94500</span>
    <span style="position:absolute;left:304px">hello@quorvin.com</span>
    <span class="phone" style="position:absolute;left:394px;font-size:8px">(555) 014-2290</span>
  </div>
  <div class="header" style="top:18px;height:36px">
    <div class="brand" style="left:78px;top:12px;font-size:10px"><i style="width:8px;height:8px"></i>quorvin</div>
    <div class="nav-item active" style="left:152px;width:32px;font-size:3.5px;padding-top:10px"><b style="width:7px;height:7px;margin-bottom:4px"></b>Home</div>
    <div class="nav-item" style="left:196px;width:26px;font-size:3.5px;padding-top:10px"><b style="width:6px;height:6px;margin-bottom:4px"></b>About</div>
    <div class="nav-item" style="left:230px;width:28px;font-size:3.5px;padding-top:10px"><b style="width:6px;height:6px;margin-bottom:4px"></b>Leasing</div>
    <div class="nav-item" style="left:266px;width:20px;font-size:3.5px;padding-top:10px"><b style="width:6px;height:6px;margin-bottom:4px"></b>FAQ</div>
    <div class="nav-item" style="left:298px;width:36px;font-size:3.5px;padding-top:10px"><b style="width:6px;height:6px;margin-bottom:4px"></b>Contact Info</div>
    <div class="cart" style="left:428px;width:24px">
      <svg width="10" height="10" viewBox="0 0 10 10"><path d="M1 2h1.5l1.2 5h4.3l1-3.5H3" fill="none" stroke="#fff" stroke-width="1"/><circle cx="4" cy="8.5" r=".7" fill="#fff"/><circle cx="7.5" cy="8.5" r=".7" fill="#fff"/></svg>
    </div>
  </div>
  <div class="backdrop" role="img" aria-label="Faint lab instruments backdrop" style="left:0;top:54px;width:560px;height:190px"></div>
  <div class="search-hint" style="left:226px;top:62px;font-size:4.4px">HELP YOU TO FIND <span>WHAT YOU ARE LOOKING !</span></div>
  <div class="search-box" style="left:352px;top:60px;width:76px;height:8px;font-size:3.5px;padding-left:4px;line-height:7px">Search keyword here</div>
  <div class="search-btn" style="left:428px;top:60px;width:24px;height:8px"></div>

  <div class="hero-title" style="left:78px;top:92px;font-size:17px">Our goal is simple:</div>
  <div class="hero-accent" style="left:78px;top:119px;font-size:14px">Save labs Time <em>&amp;</em> Money</div>
  <p class="hero-copy" style="left:78px;top:144px;width:220px;font-size:5.6px"><b>quorvin</b> is a lab support program that provides scientists with comprehensive maintenance/repair coverage and operating lease solutions at an affordable price.</p>
  <div class="btn teal" style="left:78px;top:192px;width:52px;height:16px;font-size:4.6px">Learn More</div>
  <div class="btn dark flag" style="left:134px;top:192px;width:56px;height:16px;font-size:4.6px">Request Lease</div>

  <div class="card active" style="left:78px;top:234px;width:88px;height:88px"><div class="shot" role="img" aria-label="Autoclave"></div><div class="label" style="top:64px;font-size:6px">Autoclave</div><i class="pin" style="width:8px;height:8px"></i></div>
  <div class="card" style="left:174px;top:234px;width:88px;height:88px"><div class="shot" role="img" aria-label="Lab balance"></div><div class="label" style="top:64px;font-size:6px">Lab Balance</div><i class="pin" style="width:8px;height:8px"></i></div>
  <div class="card" style="left:270px;top:234px;width:88px;height:88px"><div class="shot" role="img" aria-label="Centrifuge"></div><div class="label" style="top:64px;font-size:6px">Centrifuge</div><i class="pin" style="width:8px;height:8px"></i></div>
  <div class="card" style="left:366px;top:234px;width:88px;height:88px"><div class="shot" role="img" aria-label="Cryostat"></div><div class="label" style="top:64px;font-size:6px">Cryostat</div><i class="pin" style="width:8px;height:8px"></i></div>
  <div class="dots" style="left:252px;top:336px"><i style="width:3px;height:3px"></i><i style="width:3px;height:3px"></i><i style="width:3px;height:3px"></i><i style="width:3px;height:3px"></i></div>

  <!-- forms -->
  <div class="form" style="left:208px;top:98px;width:112px;height:164px">
    <div class="ttl" style="left:7px;top:6px;font-size:4.4px"><b>Leave Message !</b> | Request a<br>lease estimate !</div>
    <div class="tab on" style="left:7px;top:28px;width:48px;height:14px;font-size:3.8px">Leave Message</div>
    <div class="tab off flag" style="left:57px;top:28px;width:48px;height:14px;font-size:3.8px">Request a lease</div>
    <div class="sub" style="left:10px;top:54px;font-size:4.2px">Start your transaction !</div>
    <div class="field" style="left:7px;top:72px;width:98px;height:10px;font-size:3.5px">Your Full Name</div>
    <div class="field" style="left:7px;top:88px;width:98px;height:10px;font-size:3.5px">Your Email Address</div>
    <div class="field" style="left:7px;top:104px;width:98px;height:10px;font-size:3.5px">Phone Number</div>
    <div class="field" style="left:7px;top:120px;width:98px;height:10px;font-size:3.5px">Brand of Instrument</div>
    <div class="submit" style="left:7px;top:140px;width:98px;height:12px;font-size:4.2px">SUBMIT</div>
  </div>
  <div class="form" style="left:337px;top:98px;width:117px;height:190px">
    <div class="ttl" style="left:7px;top:6px;font-size:4.4px"><b>Leave Message !</b> | Request a<br>lease estimate !</div>
    <div class="tab on flag" style="left:7px;top:28px;width:50px;height:14px;font-size:3.8px">Leave Message</div>
    <div class="tab off" style="left:59px;top:28px;width:50px;height:14px;font-size:3.8px">Request a lease</div>
    <div class="sub" style="left:10px;top:54px;font-size:4.2px">Start your transaction !</div>
    <div class="field" style="left:7px;top:72px;width:102px;height:10px;font-size:3.5px">Your Full Name</div>
    <div class="field" style="left:7px;top:88px;width:102px;height:10px;font-size:3.5px">Your Email Address</div>
    <div class="field" style="left:7px;top:104px;width:102px;height:10px;font-size:3.5px">Phone Number</div>
    <div class="field" style="left:7px;top:118px;width:102px;height:38px;font-size:3.5px;align-items:flex-start;padding-top:4px">Type your message</div>
    <div class="submit" style="left:7px;top:166px;width:102px;height:12px;font-size:4.2px">SUBMIT</div>
  </div>
  <svg style="left:0;top:0" width="560" height="300" aria-hidden="true">
    <g stroke="#e23b2e" stroke-width="1.2" fill="#e23b2e">
      <line x1="192" y1="200" x2="204" y2="200"/><path d="M208 200l-5-3v6z"/>
      <line x1="168" y1="141" x2="168" y2="148" stroke="none"/>
      <line x1="289" y1="141" x2="289" y2="166"/><path d="M289 170l-3-5h6z"/>
      <line x1="366" y1="141" x2="366" y2="166"/><path d="M366 170l-3-5h6z"/>
    </g>
  </svg>

  <div class="hours-band" style="left:78px;top:366px;width:374px;height:16px;font-size:7px;line-height:16px;letter-spacing:.6em">OPERATING HOURS</div>
  <div class="hours-badge" style="left:366px;top:356px;width:36px;height:34px"></div>
  <svg style="left:376px;top:365px" width="16" height="16" aria-hidden="true"><circle cx="8" cy="8" r="6" fill="none" stroke="#33c4ad" stroke-width="1.2"/><path d="M8 4.5V8h3" fill="none" stroke="#33c4ad" stroke-width="1.2"/></svg>
  <div style="left:90px;top:396px;width:166px;font-size:5px">
    <div class="hours-row" style="padding:3px 0"><span>Monday</span><span class="t">7:00 AM - 6:00 PM</span></div>
    <div class="hours-row" style="padding:3px 0;margin-top:3px"><span>Tuesday</span><span class="t">7:00 AM - 6:00 PM</span></div>
    <div class="hours-row" style="padding:3px 0;margin-top:3px"><span>Wednesday</span><span class="t">7:00 AM - 6:00 PM</span></div>
  </div>
  <div style="left:278px;top:396px;width:166px;font-size:5px">
    <div class="hours-row" style="padding:3px 0"><span>Thursday</span><span class="t">7:00 AM - 6:00 PM</span></div>
    <div class="hours-row" style="padding:3px 0;margin-top:3px"><span>Friday</span><span class="t">7:00 AM - 6:00 PM</span></div>
    <div class="hours-row" style="padding:3px 0;margin-top:3px;border:none"><span>Saturday | Sunday</span><span class="closed">Closed</span></div>
  </div>
  <p class="caps" style="left:106px;top:457px;width:340px;font-size:5.4px;line-height:1.3"><b>Trusted company offering</b> scientific equipment service plans and flexible leases</p>
  <p class="copy" style="left:104px;top:484px;width:334px;font-size:4.2px">At <b>quorvin</b>, our goal is to ensure the success of your business. Whether you are running a laboratory or other scientific facilities, we want to keep you provided with the best in cutting-edge equipment. That's why we offer flexible scientific equipment leasing options with worry-free service plans to provide your business with the tools needed to perform at its peak.</p>
  <div class="btn teal" style="left:250px;top:530px;width:30px;height:8px;font-size:3px">View More</div>
  <p class="caps" style="left:106px;top:565px;width:340px;font-size:5.4px"><b>We understand your needs</b> because we are scientist first</p>
  <p class="copy" style="left:104px;top:584px;width:334px;font-size:4.2px">At <b>quorvin</b>, our goal is to ensure the success of your business. Whether you are running a laboratory or other scientific facilities, we want to keep you provided with the best in cutting-edge equipment. That's why we offer flexible scientific equipment leasing options.</p>
</section>

<!-- ============ PAGE 2 : LEASE / LAB BALANCE ============ -->
<section class="page lease" style="left:480px;top:128px;width:330px;height:824px">
  <div class="topbar" style="height:13px;font-size:2.8px;line-height:13px">
    <span style="position:absolute;left:55px"><i class="dot" style="width:5px;height:5px"></i><i class="dot" style="width:5px;height:5px"></i><i class="dot" style="width:5px;height:5px"></i><i class="dot" style="width:5px;height:5px"></i></span>
    <span style="position:absolute;left:108px">48 Alder Lane Suite 300 Fremont, CA 94500</span>
    <span style="position:absolute;left:212px">hello@quorvin.com</span>
    <span class="phone" style="position:absolute;left:277px;font-size:5.6px">(555) 014-2290</span>
  </div>
  <div class="header" style="top:13px;height:25px">
    <div class="brand" style="left:55px;top:8px;font-size:7px"><i style="width:5px;height:5px"></i>quorvin</div>
    <div class="nav-item" style="left:110px;width:18px;font-size:2.4px;padding-top:6px"><b style="width:4px;height:4px;margin-bottom:3px"></b>Home</div>
    <div class="nav-item" style="left:134px;width:18px;font-size:2.4px;padding-top:6px"><b style="width:4px;height:4px;margin-bottom:3px"></b>About</div>
    <div class="nav-item active" style="left:156px;width:22px;font-size:2.4px;padding-top:6px"><b style="width:4px;height:4px;margin-bottom:3px"></b>Leasing</div>
    <div class="nav-item" style="left:182px;width:14px;font-size:2.4px;padding-top:6px"><b style="width:4px;height:4px;margin-bottom:3px"></b>FAQ</div>
    <div class="nav-item" style="left:204px;width:28px;font-size:2.4px;padding-top:6px"><b style="width:4px;height:4px;margin-bottom:3px"></b>Contact Info</div>
    <div class="cart" style="left:301px;width:19px"><svg width="7" height="7" viewBox="0 0 10 10"><path d="M1 2h1.5l1.2 5h4.3l1-3.5H3" fill="none" stroke="#fff" stroke-width="1.2"/></svg></div>
  </div>
  <div class="search-hint" style="left:160px;top:43px;font-size:3px">HELP YOU TO FIND <span>WHAT YOU ARE LOOKING !</span></div>
  <div class="search-box" style="left:244px;top:42px;width:50px;height:6px;font-size:2.4px;padding-left:2px;line-height:5px">Search keyword here</div>
  <div class="search-btn" style="left:294px;top:42px;width:15px;height:6px"></div>

  <div class="hero-title" style="left:55px;top:64px;font-size:11px">Our goal is simple:</div>
  <div class="hero-accent" style="left:55px;top:82px;font-size:9px">Save labs Time <em>&amp;</em> Money</div>
  <p class="hero-copy" style="left:55px;top:100px;width:132px;font-size:3.6px"><b>quorvin</b> is a lab support program that provides scientists with comprehensive maintenance/repair coverage and operating lease solutions at an affordable price.</p>
  <div class="btn teal" style="left:55px;top:134px;width:34px;height:9px;font-size:3px">Learn More</div>
  <div class="btn dark" style="left:90px;top:134px;width:36px;height:9px;font-size:3px">Request Lease</div>
  <div class="hero-visual" role="img" aria-label="Group of lab instruments: analyser, balance and microscope" style="left:192px;top:50px;width:128px;height:86px"></div>
  <div class="dots" style="left:292px;top:140px;gap:3px"><i style="width:2px;height:2px"></i><i style="width:2px;height:2px"></i><i style="width:2px;height:2px"></i><i style="width:2px;height:2px"></i></div>

  <div class="card active" style="left:55px;top:164px;width:62px;height:62px"><div class="shot" role="img" aria-label="Autoclave"></div><div class="label" style="top:45px;font-size:4px">Autoclave</div><i class="pin" style="width:6px;height:6px"></i></div>
  <div class="card" style="left:122px;top:164px;width:62px;height:62px"><div class="shot" role="img" aria-label="Lab balance"></div><div class="label" style="top:45px;font-size:4px">Lab Balance</div><i class="pin" style="width:6px;height:6px"></i></div>
  <div class="card" style="left:189px;top:164px;width:62px;height:62px"><div class="shot" role="img" aria-label="Centrifuge"></div><div class="label" style="top:45px;font-size:4px">Centrifuge</div><i class="pin" style="width:6px;height:6px"></i></div>
  <div class="card" style="left:256px;top:164px;width:62px;height:62px"><div class="shot" role="img" aria-label="Cryostat"></div><div class="label" style="top:45px;font-size:4px">Cryostat</div><i class="pin" style="width:6px;height:6px"></i></div>
  <div class="dots" style="left:176px;top:235px;gap:3px"><i style="width:2px;height:2px"></i><i style="width:2px;height:2px"></i><i style="width:2px;height:2px"></i><i style="width:2px;height:2px"></i></div>

  <div class="side-head" style="left:55px;top:258px;width:91px;height:12px;font-size:3.4px;padding-left:4px">FEATURED PRODUCTS</div>
  <ul class="side-list" style="left:55px;top:272px;width:91px;font-size:2.6px">
    <li style="padding:3px 4px">Autoclave</li><li class="on" style="padding:3px 4px">Lab Balance</li><li style="padding:3px 4px">Centrifuge</li><li style="padding:3px 4px">Microscope</li><li style="padding:3px 4px">Cryostat</li><li style="padding:3px 4px">Next Generation Sequencer (NGS)</li><li style="padding:3px 4px">Flow Cytometers</li><li style="padding:3px 4px">PCR System</li><li style="padding:3px 4px">Liquid Handlers</li><li style="padding:3px 4px">Microplate Readers</li><li style="padding:3px 4px">Clinical Chemistry Analyzers</li><li style="padding:3px 4px">Blood Bank Analyzers</li><li style="padding:3px 4px">Peptide Synthesizers</li><li style="padding:3px 4px">Microarray Scanners</li><li style="padding:3px 4px">Spectrophotometers</li><li style="padding:3px 4px">Western Blot Imaging System</li><li style="padding:3px 4px">Liquid Chromatography Systems</li><li style="padding:3px 4px;border:none">View More</li>
  </ul>
  <div class="form" style="left:59px;top:480px;width:82px;height:10px;border:none;background:var(--panel)">
    <div class="ttl" style="left:4px;top:2px;font-size:2.8px"><b>Contact us today</b> | Request a lease estimate !</div>
  </div>
  <p class="tiny" style="left:59px;top:496px;width:82px;text-align:center">Regardless if you're looking to lease a pipette system or a sample analyzer, we can help. Call us at <b style="color:var(--teal);font-size:5px">(555) 014-2290</b> or fill out our contact form below.</p>
  <div class="form" style="left:59px;top:526px;width:82px;height:112px">
    <div class="tab on" style="left:5px;top:5px;width:35px;height:8px;font-size:2.4px">Leave Message</div>
    <div class="tab off" style="left:42px;top:5px;width:35px;height:8px;font-size:2.4px">Request a lease</div>
    <div class="sub" style="left:6px;top:20px;font-size:2.8px">Start your transaction !</div>
    <div class="field" style="left:5px;top:32px;width:72px;height:8px;font-size:2.4px">Your Full Name</div>
    <div class="field" style="left:5px;top:44px;width:72px;height:8px;font-size:2.4px">Your Email Address</div>
    <div class="field" style="left:5px;top:56px;width:72px;height:8px;font-size:2.4px">Phone Number</div>
    <div class="field" style="left:5px;top:68px;width:72px;height:8px;font-size:2.4px">Brand of Instrument</div>
    <div class="submit" style="left:5px;top:84px;width:72px;height:8px;font-size:2.8px">SUBMIT</div>
  </div>

  <div class="hero-visual" role="img" aria-label="Lab balance" style="left:154px;top:258px;width:52px;height:50px;background:linear-gradient(160deg,#fbfcfc,#bfc6c8)"></div>
  <div class="body-title" style="left:212px;top:268px;font-size:9px">Lab Balance</div>
  <p class="tiny" style="left:212px;top:283px;width:104px;letter-spacing:.1em;text-transform:uppercase">How laboratory scales work &amp; how our services save your time &amp; money</p>
  <p class="tiny" style="left:154px;top:318px;width:162px;color:#555">Here are the advantages of the quorvin lab balance leasing program:</p>
  <ul class="tiny" style="left:160px;top:330px;width:156px;list-style:none">
    <li>• Near zero upfront costs and the ability to spread out payments over time.</li>
    <li>• Payments may be fully tax deductible, which yields additional savings.</li>
    <li>• Reduction of equipment downtime through our repair coverage.</li>
    <li>• Avoid hassles of upkeep associated with equipment procurement.</li>
    <li>• Cash saved through our program can be put to work in other areas.</li>
  </ul>
  <p class="tiny" style="left:154px;top:384px;width:162px;color:#555">Please consult your tax advisor to determine the full tax implications of leasing equipment.</p>
  <p class="tiny" style="left:154px;top:404px;width:162px">A lab balance is a class of balance designed to measure small mass in the sub-milligram range. The measuring pan of an analytical balance is inside a transparent enclosure with doors so that dust does not collect and air currents in the room do not affect the balance's operation.</p>
  <p class="tiny" style="left:154px;top:432px;width:162px">This enclosure is often called a draft shield. The use of a mechanically vented balance safety enclosure, which has uniquely designed acrylic airfoils, allows smooth turbulence-free airflow that prevents balance fluctuation and the measure of mass down to 1 µg without fluctuations or loss of product.</p>
  <p class="tiny" style="left:154px;top:462px;width:162px">Also, the sample must be at room temperature to prevent natural convection from forming air currents inside the enclosure from causing an error in reading.</p>
  <div class="btn teal" style="left:213px;top:477px;width:20px;height:5px;font-size:2px">View More</div>
  <p class="caps" style="left:154px;top:490px;width:162px;font-size:3px"><b>Methods &amp; types of</b> precision weighing</p>
  <p class="tiny" style="left:154px;top:500px;width:162px">Balances can be found in nearly every laboratory setting throughout the world. Their ability to accurately measure weights and provide detailed data makes them indispensable tools.</p>
  <ul class="rows" style="left:160px;top:520px;width:150px;font-size:2.7px">
    <li style="padding:2px 2px">Microbalances &amp; Ultra Micro Balances</li><li style="padding:2px 2px">Automated Powder &amp; Liquid Dosing</li><li style="padding:2px 2px">Analytical Balances</li><li style="padding:2px 2px">Precision Balances</li><li style="padding:2px 2px">Moisture Analyzer</li><li style="padding:2px 2px">Gold and Carat Balances</li>
  </ul>
  <p class="caps" style="left:154px;top:598px;width:162px;font-size:3px"><b>An analytical balance</b> that suits your needs</p>
  <ul class="rows" style="left:160px;top:610px;width:150px;font-size:2.7px">
    <li style="padding:2px 2px">Operating Lease</li><li style="padding:2px 2px">Sale Leaseback</li><li style="padding:2px 2px">Laboratory Balance Manufacturers &amp; Models on the Market</li><li style="padding:2px 10px">Brightmass</li><li style="padding:2px 10px">Veltora</li><li style="padding:2px 10px">Kelvane</li><li style="padding:2px 10px">Harlow &amp; Finch</li><li style="padding:2px 10px">Tessaro</li><li style="padding:2px 10px">Marlow Scale</li><li style="padding:2px 10px;border:none">View More</li>
  </ul>

  <div class="footer" style="top:733px;height:81px">
    <h4 style="left:55px;top:6px;font-size:3px">Quick Links</h4>
    <div class="tiny" style="left:55px;top:16px;color:#ccc">Home<br>About Us<br>Leasing<br>FAQ<br>Contact Info</div>
    <h4 style="left:160px;top:6px;font-size:3px">Contact Info</h4>
    <div class="tiny" style="left:166px;top:16px;color:#ccc">48 Alder Lane<br>Suite 300<br>Fremont, CA 94500</div>
    <div style="left:166px;top:34px;font-size:5px;color:var(--teal)">(555) 014-2290</div>
    <div class="tiny" style="left:166px;top:42px;color:#ccc">hello@quorvin.com<br>https://quorvin.com</div>
    <h4 style="left:240px;top:6px;font-size:3px">Always receive news letter</h4>
    <div style="left:240px;top:16px;width:80px;height:6px;background:#9aa09f"></div>
    <div style="left:240px;top:24px;width:80px;height:6px;background:#9aa09f"></div>
    <div class="btn teal" style="left:240px;top:32px;width:80px;height:5px;font-size:2.4px">Subscribe</div>
    <div style="left:242px;top:42px;display:flex;gap:3px"><i style="width:5px;height:5px;border-radius:50%;background:#eee"></i><i style="width:5px;height:5px;border-radius:50%;background:#eee"></i><i style="width:5px;height:5px;border-radius:50%;background:#eee"></i><i style="width:5px;height:5px;border-radius:50%;background:#eee"></i></div>
    <div class="legal" style="top:58px;height:23px;font-size:2.6px;padding-top:4px">We are a team of scientists driven by our passion for research. Your success is our mission.<br><br>Copyright © 2018 quorvin. All Rights Reserved.</div>
  </div>
</section>

<!-- ============ PAGE 3 : HOME ============ -->
<section class="page home" style="left:810px;top:234px;width:374px;height:948px">
  <div class="topbar" style="height:14px;font-size:2.8px;line-height:14px">
    <span style="position:absolute;left:55px"><i class="dot" style="width:5px;height:5px"></i><i class="dot" style="width:5px;height:5px"></i><i class="dot" style="width:5px;height:5px"></i><i class="dot" style="width:5px;height:5px"></i></span>
    <span style="position:absolute;left:108px">48 Alder Lane Suite 300 Fremont, CA 94500</span>
    <span style="position:absolute;left:220px">hello@quorvin.com</span>
    <span class="phone" style="position:absolute;left:277px;font-size:5.6px">(555) 014-2290</span>
  </div>
  <div class="header" style="top:14px;height:24px">
    <div class="brand" style="left:55px;top:8px;font-size:7px"><i style="width:5px;height:5px"></i>quorvin</div>
    <div class="nav-item active" style="left:116px;width:20px;font-size:2.4px;padding-top:6px"><b style="width:4px;height:4px;margin-bottom:3px"></b>Home</div>
    <div class="nav-item" style="left:142px;width:18px;font-size:2.4px;padding-top:6px"><b style="width:4px;height:4px;margin-bottom:3px"></b>About</div>
    <div class="nav-item" style="left:166px;width:20px;font-size:2.4px;padding-top:6px"><b style="width:4px;height:4px;margin-bottom:3px"></b>Leasing</div>
    <div class="nav-item" style="left:192px;width:14px;font-size:2.4px;padding-top:6px"><b style="width:4px;height:4px;margin-bottom:3px"></b>FAQ</div>
    <div class="nav-item" style="left:212px;width:28px;font-size:2.4px;padding-top:6px"><b style="width:4px;height:4px;margin-bottom:3px"></b>Contact Info</div>
    <div class="cart" style="left:301px;width:18px"><svg width="7" height="7" viewBox="0 0 10 10"><path d="M1 2h1.5l1.2 5h4.3l1-3.5H3" fill="none" stroke="#fff" stroke-width="1.2"/></svg></div>
  </div>
  <div class="backdrop" role="img" aria-label="Faint lab instruments backdrop" style="left:0;top:38px;width:374px;height:120px"></div>
  <div class="search-hint" style="left:160px;top:44px;font-size:3px">HELP YOU TO FIND <span>WHAT YOU ARE LOOKING !</span></div>
  <div class="search-box" style="left:252px;top:43px;width:48px;height:6px;font-size:2.4px;padding-left:2px;line-height:5px">Search keyword here</div>
  <div class="search-btn" style="left:300px;top:43px;width:18px;height:6px"></div>

  <div class="hero-title" style="left:55px;top:64px;font-size:11px">Our goal is simple:</div>
  <div class="hero-accent" style="left:55px;top:82px;font-size:9px">Save labs Time <em>&amp;</em> Money</div>
  <p class="hero-copy" style="left:55px;top:100px;width:132px;font-size:3.6px"><b>quorvin</b> is a lab support program that provides scientists with comprehensive maintenance/repair coverage and operating lease solutions at an affordable price.</p>
  <div class="btn teal" style="left:55px;top:134px;width:38px;height:9px;font-size:3px">Learn More</div>
  <div class="btn dark" style="left:94px;top:134px;width:36px;height:9px;font-size:3px">Request Lease</div>
  <div class="hero-visual" role="img" aria-label="Group of lab instruments: analyser, balance and microscope" style="left:190px;top:50px;width:120px;height:84px"></div>
  <div class="dots" style="left:294px;top:139px;gap:3px"><i style="width:2px;height:2px"></i><i style="width:2px;height:2px"></i><i style="width:2px;height:2px"></i><i style="width:2px;height:2px"></i></div>

  <div class="card active" style="left:55px;top:164px;width:62px;height:62px"><div class="shot" role="img" aria-label="Autoclave"></div><div class="label" style="top:45px;font-size:4px">Autoclave</div><i class="pin" style="width:6px;height:6px"></i></div>
  <div class="card" style="left:122px;top:164px;width:62px;height:62px"><div class="shot" role="img" aria-label="Lab balance"></div><div class="label" style="top:45px;font-size:4px">Lab Balance</div><i class="pin" style="width:6px;height:6px"></i></div>
  <div class="card" style="left:189px;top:164px;width:62px;height:62px"><div class="shot" role="img" aria-label="Centrifuge"></div><div class="label" style="top:45px;font-size:4px">Centrifuge</div><i class="pin" style="width:6px;height:6px"></i></div>
  <div class="card" style="left:256px;top:164px;width:62px;height:62px"><div class="shot" role="img" aria-label="Cryostat"></div><div class="label" style="top:45px;font-size:4px">Cryostat</div><i class="pin" style="width:6px;height:6px"></i></div>
  <div class="dots" style="left:176px;top:236px;gap:3px"><i style="width:2px;height:2px"></i><i style="width:2px;height:2px"></i><i style="width:2px;height:2px"></i><i style="width:2px;height:2px"></i></div>

  <div class="hours-band" style="left:55px;top:256px;width:263px;height:12px;font-size:4.6px;line-height:12px;letter-spacing:.6em">OPERATING HOURS</div>
  <div class="hours-badge" style="left:254px;top:248px;width:26px;height:24px"></div>
  <svg style="left:261px;top:254px" width="12" height="12" aria-hidden="true"><circle cx="6" cy="6" r="4.5" fill="none" stroke="#33c4ad" stroke-width="1"/><path d="M6 3.5V6h2" fill="none" stroke="#33c4ad" stroke-width="1"/></svg>
  <div style="left:62px;top:277px;width:118px;font-size:3.2px">
    <div class="hours-row" style="padding:2px 0"><span>Monday</span><span class="t">7:00 AM - 6:00 PM</span></div>
    <div class="hours-row" style="padding:2px 0;margin-top:2px"><span>Tuesday</span><span class="t">7:00 AM - 6:00 PM</span></div>
    <div class="hours-row" style="padding:2px 0;margin-top:2px"><span>Wednesday</span><span class="t">7:00 AM - 6:00 PM</span></div>
  </div>
  <div style="left:196px;top:277px;width:118px;font-size:3.2px">
    <div class="hours-row" style="padding:2px 0"><span>Thursday</span><span class="t">7:00 AM - 6:00 PM</span></div>
    <div class="hours-row" style="padding:2px 0;margin-top:2px"><span>Friday</span><span class="t">7:00 AM - 6:00 PM</span></div>
    <div class="hours-row" style="padding:2px 0;margin-top:2px;border:none"><span>Saturday | Sunday</span><span class="closed">Closed</span></div>
  </div>
  <p class="caps" style="left:75px;top:320px;width:240px;font-size:3.6px;line-height:1.3"><b>Trusted company offering</b> scientific equipment service plans and flexible leases</p>
  <p class="tiny" style="left:75px;top:338px;width:240px">At quorvin, our goal is to ensure the success of your business. Whether you are running a laboratory or other scientific facilities, we want to keep you provided with the best in cutting-edge equipment. That's why we offer flexible scientific equipment leasing options with worry-free service plans to provide your business with the tools needed to perform at its peak.</p>
  <div class="btn teal" style="left:178px;top:372px;width:20px;height:5px;font-size:2px">View More</div>
  <p class="caps" style="left:75px;top:395px;width:240px;font-size:3.6px"><b>We understand your needs</b> because we are scientist first</p>
  <p class="tiny" style="left:75px;top:406px;width:240px">At quorvin, our goal is to ensure the success of your business. Whether you are running a laboratory or other scientific facilities, we want to keep you provided with the best in cutting-edge equipment. That's why we offer flexible leasing options with worry-free service plans.</p>
  <svg style="left:164px;top:437px" width="44" height="44" aria-hidden="true"><circle cx="22" cy="22" r="20" fill="#fff" stroke="#d6e2df"/><circle cx="22" cy="22" r="14" fill="none" stroke="#33c4ad" stroke-width="3"/><circle cx="22" cy="22" r="9" fill="#3a3c40"/></svg>
  <p class="tiny" style="left:75px;top:492px;width:112px">When it comes to creating innovative solutions that cater to your lab, quorvin's dedicated team of problem solvers has got you covered. Here's how we save you time and money.</p>
  <div class="btn teal" style="left:168px;top:518px;width:18px;height:4px;font-size:1.8px">Learn More</div>
  <p class="tiny" style="left:198px;top:492px;width:118px">We regularly provide businesses with what they need to improve their budget and efficiency. We offer laboratory equipment leasing for a wide range of needs. If you want to discuss your needs, don't hesitate to call us at <b style="color:var(--teal);font-size:4.4px">(555) 014-2290</b> or fill out our <span style="color:var(--teal)">Contact Form</span>.</p>

  <p class="caps" style="left:75px;top:550px;font-size:3.6px"><b>Our</b> skills</p>
  <div class="skill-icon" style="left:133px;top:570px;width:16px;height:16px"></div>
  <p class="tiny" style="left:100px;top:590px;width:82px;text-align:center">Knowledge of the laboratory<br><span style="color:var(--teal)">View →</span></p>
  <div class="skill-icon" style="left:133px;top:620px;width:16px;height:16px"></div>
  <p class="tiny" style="left:100px;top:640px;width:82px;text-align:center">Worry free lab equipment PM/repair coverage<br><span style="color:var(--teal)">View →</span></p>
  <div class="skill-icon" style="left:133px;top:670px;width:16px;height:16px"></div>
  <p class="tiny" style="left:100px;top:690px;width:82px;text-align:center">Cost-effective lease structures and payment plans<br><span style="color:var(--teal)">View →</span></p>
  <div role="img" aria-label="Illustration of climbing steps toward a target" style="left:182px;top:570px;width:72px;height:60px;background:linear-gradient(135deg,#f6f9f8 0%,#f6c66a 50%,#57c08f 100%);border-radius:3px"></div>
  <div style="left:184px;top:648px;width:112px">
    <p class="tiny" style="color:#555">Cost Saving</p><div class="progress"><i style="width:95%"></i></div>
    <p class="tiny" style="color:#555;margin-top:2px">Lease Plan Flexibility</p><div class="progress"><i style="width:88%"></i></div>
    <p class="tiny" style="color:#555;margin-top:2px">Customer Service</p><div class="progress"><i style="width:100%"></i></div>
    <p class="tiny" style="color:#555;margin-top:6px;font-weight:700">The Competition</p>
    <p class="tiny" style="color:#555">Scheduling</p><div class="progress"><i style="width:40%"></i></div>
    <p class="tiny" style="color:#555;margin-top:2px">Continued Support</p><div class="progress"><i style="width:30%"></i></div>
  </div>

  <div class="photo" role="img" aria-label="Black and white city skyline backdrop" style="left:55px;top:729px;width:263px;height:105px"></div>
  <div style="left:55px;top:734px;width:263px;text-align:center;color:#fff;font-weight:700;font-size:11px;letter-spacing:.25em">THE TOP MANAGEMENT</div>
  <div class="avatar" role="img" aria-label="Team member portrait" style="left:78px;top:760px;width:16px;height:16px"></div>
  <div class="avatar" role="img" aria-label="Team member portrait" style="left:171px;top:760px;width:16px;height:16px"></div>
  <div class="avatar" role="img" aria-label="Team member portrait" style="left:262px;top:760px;width:16px;height:16px"></div>
  <p class="tiny" style="left:62px;top:780px;width:70px;text-align:center;color:#fff"><b style="color:var(--teal)">Dana Reyes</b><br>Lab Relations<br>"In this short time at the lab I've opened my eyes to the passion and dedication that drives our team every day."</p>
  <p class="tiny" style="left:152px;top:780px;width:70px;text-align:center;color:#fff"><b style="color:var(--teal)">Owen Marsh</b><br>Finance<br>"Our success is measured by our customers' success. We care about their budgets and the future of their work."</p>
  <p class="tiny" style="left:242px;top:780px;width:70px;text-align:center;color:#fff"><b style="color:var(--teal)">Iris Coleman</b><br>Operations<br>"The core of my involvement is helping labs succeed through an effective operational plan."</p>

  <div class="footer" style="top:869px;height:79px">
    <div class="brand" style="left:55px;top:6px;font-size:5px"><i style="width:4px;height:4px"></i>quorvin</div>
    <p class="tiny" style="left:55px;top:16px;width:80px;color:#bbb">We are a team of scientists driven by our passion for research. We strive to serve the scientific community and help labs grow.</p>
    <h4 style="left:153px;top:6px;font-size:3px">Quick Links</h4>
    <div class="tiny" style="left:153px;top:14px;color:#ccc">Home<br>About Us<br>Leasing<br>FAQ<br>Contact Info</div>
    <h4 style="left:200px;top:6px;font-size:3px">Contact Info</h4>
    <div class="tiny" style="left:206px;top:14px;color:#ccc">48 Alder Lane<br>Suite 300<br>Fremont, CA 94500</div>
    <div style="left:206px;top:32px;font-size:5px;color:var(--teal)">(555) 014-2290</div>
    <div class="tiny" style="left:206px;top:40px;color:#ccc">hello@quorvin.com<br>https://quorvin.com</div>
    <h4 style="left:262px;top:6px;font-size:3px">Always receive news letter</h4>
    <div style="left:262px;top:14px;width:78px;height:6px;background:#9aa09f"></div>
    <div style="left:262px;top:22px;width:78px;height:6px;background:#9aa09f"></div>
    <div class="btn teal" style="left:262px;top:30px;width:78px;height:5px;font-size:2.4px">Subscribe</div>
    <div style="left:264px;top:40px;display:flex;gap:3px"><i style="width:5px;height:5px;border-radius:50%;background:#eee"></i><i style="width:5px;height:5px;border-radius:50%;background:#eee"></i><i style="width:5px;height:5px;border-radius:50%;background:#eee"></i><i style="width:5px;height:5px;border-radius:50%;background:#eee"></i></div>
    <div class="legal" style="top:56px;height:23px;font-size:2.6px;padding-top:4px">We are a team of scientists driven by our passion for research. Your success is our mission.<br><br>Copyright © 2018 quorvin. All Rights Reserved.</div>
  </div>
</section>

<div class="badge-num" style="position:absolute;left:523px;top:11px">1</div>
<div class="badge-num" style="position:absolute;left:827px;top:119px">2</div>
<div class="badge-num" style="position:absolute;left:1138px;top:224px">3</div>

<div class="legend">
  <p style="top:24px"><b>1. Landing Page</b> - Click Request Lease Button and</p>
  <p style="top:64px"><span>- View Messanging form</span></p>
  <p style="top:104px"><b>2. Home Page</b><span>- Full Page</span></p>
  <p style="top:144px"><b>3. Lease Page</b><span>- Lab Balance</span></p>
</div>

</div>
</body>
</html>
```